Industrial Company needing new business cards

We are a newly branded Industrial trade company. We specialise in Electrical, Mechanical and Air-conditioning.

I would like to see designs single sided. Focusing on the color scheme white/red/black and possibly gray. Possibly make it a black card with white writting... but open to all designs.

I would like the design to be professional, sleek and to the point.

Industry/Entity Type

Business

Contact Information for Business Card

Tom Harwell
Managing Director / Electrician
tomwork@vandilo.com.au
417 Calloway Street, Pembrook NSW 2458
Mobile: 0497551832
www.harwellindustrialgroup.com.au

Requirements
Must have
• Must be able to be sent in a manner that i can change the details for each employee.
• Our logo
Nice to have
• Would like it to somehow have " incorporating Barvo Group Pty Ltd" as this is the company we have taken over.
Should not have
• No yellow!!!
• must not simply place "barvo group" randomly on the business card. refer nice to have.

```html
<!DOCTYPE html>
<html lang="en">
<head>
<meta charset="utf-8">
<title>Harwell Industrial Group – Business Card</title>
<link rel="stylesheet" href="https://fonts.googleapis.com/css2?family=Montserrat:wght@600;700&family=Open+Sans:wght@400;600&family=Roboto+Condensed:wght@400&display=swap">
<style>
  :root {
    --stage: #e9e4de;
    --card: #f6f6f5;
    --ink: #1a1a1a;
    --red: #c8191e;
    --deep-red: #6e1216;
    --black: #111111;
    --grey: #7a7a7a;
    --contact: #d9d4cf;
  }
  * { margin: 0; padding: 0; box-sizing: border-box; }
  html, body {
    width: 1200px;
    height: 970px;
    overflow: hidden;
    background: var(--stage);
  }
  .card {
    position: absolute;
    left: 172px;
    top: 270px;
    width: 856px;
    height: 476px;
    background: var(--card);
    overflow: hidden;
    box-shadow: 0 6px 24px rgba(0,0,0,0.12);
  }
  .card-band {
    position: absolute;
    left: 0;
    right: 0;
    top: 322px;
    bottom: 0;
    background: linear-gradient(90deg, var(--deep-red) 0%, #2a1112 40%, var(--black) 65%);
  }
  .brand {
    position: absolute;
    left: 300px;
    top: 72px;
    display: flex;
    align-items: center;
    gap: 22px;
  }
  .brand-mark {
    width: 64px;
    height: 64px;
    background: var(--red);
  }
  .brand-name {
    font-family: "Montserrat", sans-serif;
    font-weight: 700;
    font-size: 25px;
    line-height: 28px;
    letter-spacing: 0.5px;
    color: var(--ink);
    text-transform: uppercase;
  }
  .brand-services {
    position: absolute;
    left: 228px;
    top: 160px;
    font-family: "Montserrat", sans-serif;
    font-weight: 600;
    font-size: 14px;
    letter-spacing: 0.6px;
    color: var(--grey);
    text-transform: uppercase;
  }
  .person {
    position: absolute;
    left: 60px;
    top: 255px;
    font-family: "Open Sans", sans-serif;
  }
  .person-name {
    font-weight: 600;
    font-size: 25px;
    color: var(--red);
    letter-spacing: 0.3px;
  }
  .person-role {
    margin-top: 4px;
    font-size: 16px;
    color: var(--ink);
  }
  .contacts {
    position: absolute;
    right: 34px;
    top: 323px;
    list-style: none;
    font-family: "Roboto Condensed", sans-serif;
    font-size: 18px;
    color: var(--contact);
    text-align: right;
  }
  .contacts li {
    display: flex;
    justify-content: flex-end;
    align-items: center;
    gap: 10px;
    height: 28.5px;
  }
  .contacts .contact-icon {
    width: 15px;
    height: 15px;
    flex: none;
  }
  .contacts .contact-address {
    margin-top: 8px;
    font-size: 19px;
  }
</style>
</head>
<body>
  <article class="card">
    <div class="card-band" role="img" aria-label="Decorative red and black swoosh band across the lower card"></div>

    <div class="brand">
      <span class="brand-mark"></span>
      <span class="brand-name">Harwell<br>Industrial<br>Group</span>
    </div>
    <p class="brand-services">Electrical - Mechanical - Airconditioning</p>

    <div class="person">
      <p class="person-name">Tom Harwell</p>
      <p class="person-role">Managing Director / Electrician</p>
    </div>

    <ul class="contacts">
      <li>0497551832
        <svg class="contact-icon" viewBox="0 0 16 16"><path fill="#c8191e" d="M2 5c0-2 2-3 6-3s6 1 6 3v1h-3V5H5v1H2zM4 7h8l2 7H2z"/></svg>
      </li>
      <li>tomwork@vandilo.com.au
        <svg class="contact-icon" viewBox="0 0 16 16"><path fill="#c8191e" d="M1 3h14v10H1zM2 4l6 5 6-5" stroke="#111" stroke-width="1"/></svg>
      </li>
      <li>harwellindustrialgroup.com.au
        <svg class="contact-icon" viewBox="0 0 16 16"><circle cx="8" cy="8" r="7" fill="#c8191e"/><path d="M1 8h14M8 1v14M3 4h10M3 12h10" stroke="#111" stroke-width="0.8" fill="none"/></svg>
      </li>
      <li class="contact-address">417 Calloway Street, Pembrook NSW 2458</li>
    </ul>
  </article>
</body>
</html>
```